Steady Valve Systems

I need a business card with the attached logo.
The second page I have attached is what we are looking for. We want doubles sided. We would like the blues fading and the logo on the back.

Industry/Entity Type

Business

```html
<!DOCTYPE html>
<html lang="en">
<head>
<meta charset="utf-8">
<title>Steady Valve Systems – Business Cards</title>
<link href="https://fonts.googleapis.com/css2?family=Mulish:wght@400;700;800&display=swap" rel="stylesheet">
<style>
  :root {
    --stage: #0c0c0d;
    --brand-blue: #1f4f9e;
    --ink-blue: #2a3f8f;
    --fade-top: #ecebf5;
    --fade-mid: #8a84c6;
    --fade-bottom: #2f2a96;
    --paper: #ffffff;
    --white-ink: #ffffff;
    --soft-ink: #e4e2f4;
  }
  * { margin: 0; padding: 0; box-sizing: border-box; }
  html, body {
    width: 1200px; height: 900px; overflow: hidden;
    background: var(--stage);
    font-family: "Mulish", "Century Gothic", sans-serif;
  }
  .canvas {
    position: relative; width: 1200px; height: 900px;
    display: flex; align-items: center; justify-content: center; gap: 70px;
  }
  .card {
    position: relative; width: 500px; height: 286px; border-radius: 3px; overflow: hidden;
  }
  .wordmark {
    color: var(--brand-blue); font-weight: 800; letter-spacing: 0.04em;
    text-transform: uppercase; line-height: 1;
  }

  /* Front: contact side with fading blues */
  .card--front {
    background: linear-gradient(160deg, var(--fade-top) 0%, var(--fade-mid) 40%, var(--fade-bottom) 100%);
    padding: 30px 36px;
  }
  .card--front .wordmark { font-size: 27px; }
  .person { margin-top: 40px; margin-left: 70px; color: var(--white-ink); }
  .person__name { font-size: 25px; font-weight: 800; }
  .person__title { font-size: 13px; color: var(--soft-ink); margin-top: 2px; }
  .contact {
    margin-top: 14px; display: grid; grid-template-columns: 22px 1fr; column-gap: 12px;
  }
  .contact__icons {
    display: flex; flex-direction: column; gap: 8px; padding-top: 4px;
    border-right: 1px solid rgba(255,255,255,0.7); padding-right: 8px;
  }
  .contact__lines { color: var(--white-ink); font-size: 18px; line-height: 1.35; }

  /* Back: logo side on white */
  .card--back {
    background: var(--paper);
    display: flex; flex-direction: column; align-items: center; justify-content: center;
  }
  .card--back .wordmark { font-size: 40px; }
  .address {
    margin-top: 34px; color: var(--ink-blue); font-size: 14px; text-align: center; line-height: 1.7;
  }
  .address span + span { margin-left: 26px; }
</style>
</head>
<body>
<main class="canvas">
  <section class="card card--front" aria-label="Business card front">
    <div class="wordmark">Steady Valve Systems</div>
    <div class="person">
      <div class="person__name">Dana R Whitley</div>
      <div class="person__title">Managing Director</div>
      <div class="contact">
        <div class="contact__icons">
          <svg width="14" height="11" viewBox="0 0 14 11" aria-label="Email">
            <rect x="0.5" y="0.5" width="13" height="10" fill="none" stroke="#fff"/>
            <path d="M0.5 0.5 L7 6 L13.5 0.5" fill="none" stroke="#fff"/>
          </svg>
          <svg width="14" height="14" viewBox="0 0 14 14" aria-label="Phone">
            <circle cx="7" cy="7" r="6.3" fill="none" stroke="#fff"/>
            <path d="M5 4 q-1 3 2 6 l1.2 -1.2 l-1.2 -1 l-0.7 0.5 q-1 -1 -1 -2 l0.6 -0.6 l-0.6 -1.4z" fill="#fff"/>
          </svg>
        </div>
        <div class="contact__lines">
          <div>dwhitley@steadyvalve.com</div>
          <div>555.0142.0386</div>
          <div>555.014.2277</div>
        </div>
      </div>
    </div>
  </section>

  <section class="card card--back" aria-label="Business card back">
    <div class="wordmark">Steady Valve Systems</div>
    <div class="address">
      <div><span>410 Harbor Lane</span><span>P.O. Box 52714</span><span>Riverton, OH 45012</span></div>
      <div>www.steadyvalve.com</div>
    </div>
  </section>
</main>
</body>
</html>
```